Email Signatures

I would like to create a new email signature for my team. The design will be the same for everyone, with only individual details such as name and email changing. You can also see our brand style on our website. https://www.rwpharbourjoinery.com.au/

Target Market(s)

Clients for new builds or renovations

Industry/Entity Type

Construction

Colors

Designer to choose colors to be used in the design.

```html
<!DOCTYPE html>
<html lang="en">
<head>
<meta charset="utf-8">
<title>RWP Harbour Joinery – Email Signatures</title>
<link href="https://fonts.googleapis.com/css2?family=Playfair+Display:ital,wght@1,700&family=Roboto:wght@400;500;700&display=swap" rel="stylesheet">
<style>
  :root {
    --stage: #dcdcdc;
    --brand-green: #18964a;
    --ink: #1f1f1f;
    --paper: #ffffff;
    --title-ink: #2a2a2a;
  }
  * { box-sizing: border-box; margin: 0; padding: 0; }
  html, body { width: 1200px; height: 977px; overflow: hidden; }
  body {
    background: var(--stage);
    font-family: "Roboto", Arial, sans-serif;
    position: relative;
  }
  .version-title {
    position: absolute;
    left: 0; width: 1200px;
    text-align: center;
    font-family: "Playfair Display", Georgia, serif;
    font-style: italic;
    font-weight: 700;
    font-size: 38px;
    color: var(--title-ink);
    text-shadow: 2px 3px 4px rgba(0,0,0,.35);
  }
  .version-title--light { top: 56px; }
  .version-title--dark { top: 880px; }

  .signature {
    position: absolute;
    left: 111px;
    width: 979px;
    height: 327px;
    overflow: hidden;
    box-shadow: 0 12px 18px rgba(0,0,0,.45);
  }
  .signature--light { top: 128px; background: var(--paper); --text: var(--ink); --swoosh: var(--ink); }
  .signature--dark { top: 516px; background: var(--ink); --text: var(--paper); --swoosh: var(--paper); }

  .signature__wave { position: absolute; inset: 0; }
  .signature__wave .band { fill: var(--brand-green); }
  .signature__wave .swoosh { fill: var(--swoosh); }

  .company-name {
    position: absolute;
    left: 98px; top: 104px;
    width: 280px;
    text-align: center;
    font-weight: 700;
    font-size: 34px;
    line-height: 1.15;
    letter-spacing: 1px;
    color: var(--text);
  }

  .divider {
    position: absolute;
    left: 489px; top: 35px;
    width: 1.5px; height: 241px;
    background: var(--brand-green);
  }

  .social-links {
    position: absolute;
    left: 30px; top: 283px;
    display: flex; gap: 8px;
  }
  .social-links span {
    width: 17px; height: 17px;
    border-radius: 50%;
    border: 2px solid var(--paper);
  }

  .person { position: absolute; left: 608px; top: 80px; }
  .person__name {
    font-weight: 700;
    font-size: 42px;
    line-height: 1;
    color: var(--brand-green);
    letter-spacing: .5px;
  }
  .person__role {
    margin-top: 2px;
    font-size: 19px;
    color: var(--text);
    letter-spacing: .5px;
  }

  .contact-list {
    position: absolute;
    left: 616px; top: 173px;
    list-style: none;
  }
  .contact-list li {
    display: flex; align-items: center;
    height: 26px;
    font-size: 19px;
    letter-spacing: .6px;
    color: var(--text);
  }
  .contact-list svg { width: 16px; height: 16px; margin-right: 12px; flex: none; }
  .contact-list svg * { fill: none; stroke: var(--brand-green); stroke-width: 2; stroke-linecap: round; stroke-linejoin: round; }
</style>
</head>
<body>

<h2 class="version-title version-title--light">White Version</h2>

<section class="signature signature--light">
  <svg class="signature__wave" viewBox="0 0 979 327" preserveAspectRatio="none" aria-hidden="true">
    <path class="band" d="M0,229 C200,270 480,298 700,302 C830,304 930,301 979,299 L979,327 L0,327 Z"/>
    <path class="swoosh" d="M331,274 C520,292 760,300 979,277 L979,290 C760,306 520,300 331,274 Z"/>
  </svg>
  <div class="company-name">RWP HARBOUR<br>JOINERY</div>
  <div class="social-links"><span></span><span></span><span></span><span></span><span></span></div>
  <div class="divider"></div>
  <div class="person">
    <p class="person__name">Liam Thornbury</p>
    <p class="person__role">General Manager</p>
  </div>
  <ul class="contact-list">
    <li><svg viewBox="0 0 16 16"><path d="M3,2 L6,2 L7,5 L5.5,6.5 C6.5,8.5 7.5,9.5 9.5,10.5 L11,9 L14,10 L14,13 C8,13.5 2.5,8 3,2 Z"/></svg>0412 555 038</li>
    <li><svg viewBox="0 0 16 16"><circle cx="8" cy="8" r="6.5"/><path d="M1.5,8 H14.5 M8,1.5 C5,5 5,11 8,14.5 M8,1.5 C11,5 11,11 8,14.5"/></svg>www.rwpharbourjoinery.com.au</li>
    <li><svg viewBox="0 0 16 16"><rect x="1.5" y="3.5" width="13" height="10" rx="1"/><path d="M1.5,4 L8,9 L14.5,4"/></svg>info@rwpharbourjoinery.com.au</li>
  </ul>
</section>

<section class="signature signature--dark">
  <svg class="signature__wave" viewBox="0 0 979 327" preserveAspectRatio="none" aria-hidden="true">
    <path class="band" d="M0,229 C200,270 480,298 700,302 C830,304 930,301 979,299 L979,327 L0,327 Z"/>
    <path class="swoosh" d="M331,274 C520,292 760,300 979,277 L979,290 C760,306 520,300 331,274 Z"/>
  </svg>
  <div class="company-name">RWP HARBOUR<br>JOINERY</div>
  <div class="social-links"><span></span><span></span><span></span><span></span><span></span></div>
  <div class="divider"></div>
  <div class="person">
    <p class="person__name">Liam Thornbury</p>
    <p class="person__role">General Manager</p>
  </div>
  <ul class="contact-list">
    <li><svg viewBox="0 0 16 16"><path d="M3,2 L6,2 L7,5 L5.5,6.5 C6.5,8.5 7.5,9.5 9.5,10.5 L11,9 L14,10 L14,13 C8,13.5 2.5,8 3,2 Z"/></svg>0412 555 038</li>
    <li><svg viewBox="0 0 16 16"><circle cx="8" cy="8" r="6.5"/><path d="M1.5,8 H14.5 M8,1.5 C5,5 5,11 8,14.5 M8,1.5 C11,5 11,11 8,14.5"/></svg>www.rwpharbourjoinery.com.au</li>
    <li><svg viewBox="0 0 16 16"><rect x="1.5" y="3.5" width="13" height="10" rx="1"/><path d="M1.5,4 L8,9 L14.5,4"/></svg>info@rwpharbourjoinery.com.au</li>
  </ul>
</section>

<h2 class="version-title version-title--dark">Black Version</h2>

</body>
</html>
```